Business Card Design Project

Business and Appointment Card for Medical Practice. On back of card we would like to have: blank line for patient name, Mon-Fri each with a check box next to the day, blank line for appointment date, blank line for appointment time, with option to circle am or pm.

Target Market(s)

Professional Business Associates, as well as function as patient appointment cards (on back side of card)

Industry/Entity Type

Business

Colors

```html
<!DOCTYPE html>
<html lang="en">
<head>
<meta charset="utf-8">
<title>Maple Grove Medical Associates – Business &amp; Appointment Cards</title>
<link rel="stylesheet" href="https://fonts.googleapis.com/css2?family=Lato:wght@400;700;900&display=swap">
<style>
  :root {
    --bg: #2a2a2a;
    --card: #fbfbfb;
    --red: #8e1b1f;
    --green: #1f6b2f;
    --ink: #4a4a4a;
    --grey: #6d6d6d;
    --rule: #3a3a3a;
  }
  * { box-sizing: border-box; margin: 0; padding: 0; }
  html, body { width: 1200px; height: 900px; overflow: hidden; }
  body { background: var(--bg); font-family: "Lato", sans-serif; position: relative; }

  .card {
    position: absolute;
    width: 640px; height: 366px;
    background: var(--card);
    box-shadow: 0 18px 40px rgba(0,0,0,.55);
    overflow: hidden;
  }
  .card--appointment { left: 80px; top: 70px; }
  .card--business { left: 480px; top: 464px; }

  /* shared brand wordmark */
  .wordmark { display: flex; align-items: center; gap: 12px; color: var(--green); font-weight: 900; }
  .wordmark__dot { width: 16px; height: 16px; border-radius: 50%; background: var(--green); flex: none; }
  .wordmark__text { line-height: 1.05; letter-spacing: .5px; white-space: nowrap; }

  /* appointment side */
  .card--appointment .wordmark { position: absolute; left: 34px; top: 40px; font-size: 22px; }
  .pill {
    position: absolute; right: 34px; top: 34px;
    background: var(--red); color: #fff;
    font-size: 17px; letter-spacing: 2px; text-transform: uppercase;
    padding: 7px 24px; border-radius: 20px;
  }
  .rule { position: absolute; height: 2px; background: var(--rule); }
  .rule--top { left: 34px; right: 34px; top: 120px; }
  .field-label { position: absolute; font-weight: 700; font-size: 18px; }
  .label--patient { left: 34px; top: 134px; color: var(--green); }
  .rule--patient { left: 160px; right: 34px; top: 156px; height: 1.5px; }

  .days { position: absolute; left: 34px; right: 34px; top: 190px; display: flex; justify-content: space-between; }
  .day { display: flex; align-items: center; gap: 8px; font-weight: 700; font-size: 18px; }
  .day:nth-child(odd) { color: var(--red); }
  .day:nth-child(even) { color: var(--green); }
  .checkbox { width: 24px; height: 24px; border: 2.5px solid var(--rule); border-radius: 5px; background: #fff; }

  .label--date { left: 34px; top: 268px; color: var(--green); }
  .rule--date { left: 92px; width: 210px; top: 290px; height: 1.5px; }
  .label--time { left: 330px; top: 268px; color: var(--red); }
  .rule--time { left: 388px; right: 34px; top: 290px; height: 1.5px; }
  .label--am { left: 470px; top: 300px; color: var(--green); }
  .label--pm { left: 560px; top: 300px; color: var(--red); }

  /* business side */
  .card--business .wordmark { position: absolute; left: 36px; top: 152px; font-size: 26px; }
  .divider {
    position: absolute; left: 338px; top: 30px; width: 4px; height: 300px;
    background: linear-gradient(to bottom, rgba(110,110,110,0), #9a9a9a 40%, #6b6b6b 85%, rgba(110,110,110,0));
  }
  .contact { position: absolute; left: 366px; top: 40px; right: 22px; }
  .contact__name { color: var(--red); font-weight: 900; font-size: 19px; }
  .contact__role { color: var(--grey); font-size: 12px; letter-spacing: 1px; text-transform: uppercase; margin-top: 2px; }
  .contact__address { color: var(--red); font-weight: 700; font-size: 15px; line-height: 1.3; margin-top: 38px; }
  .contact__list { list-style: none; margin-top: 10px; }
  .contact__item { display: flex; align-items: center; gap: 12px; color: var(--ink); font-size: 15px; height: 27px; white-space: nowrap; }
  .contact__item svg { width: 18px; height: 18px; fill: var(--grey); flex: none; }
  .contact__web { color: var(--red); font-weight: 900; font-size: 15px; margin-top: 10px; white-space: nowrap; }
</style>
</head>
<body>

<section class="card card--appointment" aria-label="Appointment card">
  <div class="wordmark"><span class="wordmark__dot"></span><span class="wordmark__text">Maple Grove<br>Medical Associates</span></div>
  <div class="pill">Appointment Card</div>
  <div class="rule rule--top"></div>

  <span class="field-label label--patient">Patient Name</span>
  <div class="rule rule--patient"></div>

  <div class="days">
    <div class="day">Mon <span class="checkbox"></span></div>
    <div class="day">Tue <span class="checkbox"></span></div>
    <div class="day">Wed <span class="checkbox"></span></div>
    <div class="day">Thu <span class="checkbox"></span></div>
    <div class="day">Fri <span class="checkbox"></span></div>
  </div>

  <span class="field-label label--date">Date:</span>
  <div class="rule rule--date"></div>
  <span class="field-label label--time">Time:</span>
  <div class="rule rule--time"></div>
  <span class="field-label label--am">AM</span>
  <span class="field-label label--pm">PM</span>
</section>

<section class="card card--business" aria-label="Business card">
  <div class="wordmark"><span class="wordmark__dot"></span><span class="wordmark__text">Maple Grove<br>Medical Associates</span></div>
  <div class="divider"></div>

  <div class="contact">
    <div class="contact__name">YOUR NAME</div>
    <div class="contact__role">Designation</div>
    <div class="contact__address">12 Rue des Lilas,<br>93100 Montreuil</div>
    <ul class="contact__list">
      <li class="contact__item">
        <svg viewBox="0 0 24 24" aria-hidden="true"><path d="M3 9c0-3 4-5 9-5s9 2 9 5v2h-5V9c-1-.6-2.5-1-4-1s-3 .4-4 1v2H3z M6 13h12l2 7H4z"/></svg>
        +33 (0)1 40 26 58 13
      </li>
      <li class="contact__item">
        <svg viewBox="0 0 24 24" aria-hidden="true"><path d="M7 2h10a1 1 0 0 1 1 1v18a1 1 0 0 1-1 1H7a1 1 0 0 1-1-1V3a1 1 0 0 1 1-1zm1 3v13h8V5zm4 14.2a.9.9 0 1 0 0 1.8.9.9 0 0 0 0-1.8z"/></svg>
        +33 (0)6 51 90 xx xx
      </li>
      <li class="contact__item">
        <svg viewBox="0 0 24 24" aria-hidden="true"><path d="M7 3h10v5H7z M3 9h18v8h-3v-3H6v3H3z M7 15h10v6H7z"/></svg>
        +33 (0)1 40 26 58 14
      </li>
      <li class="contact__item">
        <svg viewBox="0 0 24 24" aria-hidden="true"><path d="M2 5h20v14H2z M3.5 6.5 12 13l8.5-6.5" stroke="#fff" stroke-width="1.4"/></svg>
        info@maplegrovemedical.com
      </li>
    </ul>
    <div class="contact__web">www.maplegrovemedical.com</div>
  </div>
</section>

</body>
</html>
```